Hey, we loved your business cards ... now we require a A6 postcard please that fits our brand and communicates our new and exciting "Happy Hour" offer. The offer is BUY ONE GET ONE FREE on the entire drinks menu (excluding champagne), SUNDAY-FRIDAY from opening until 8pm. A clear map on the reverse with our full contact details is required please.

```html
<!DOCTYPE html>
<html lang="en">
<head>
<meta charset="utf-8">
<title>Happy Hour – Lantern 27</title>
<link rel="stylesheet" href="https://fonts.googleapis.com/css2?family=Pacifico&family=Open+Sans:wght@400;600;700;800&display=swap">
<style>
  :root {
    --backdrop: #f1f1f1;
    --navy: #0a1f6b;
    --royal: #0a52e0;
    --sky: #5a8cff;
    --violet: #6a2aa8;
    --magenta: #d8349a;
    --glow: #ffffff;
    --offer-green: #77ff00;
    --ink: #111111;
    --map-tone-a: rgba(245, 215, 170, 0.35);
    --map-tone-b: rgba(150, 40, 40, 0.35);
  }
  html, body {
    margin: 0;
    width: 1200px;
    height: 1000px;
    overflow: hidden;
    background: var(--backdrop);
  }
  .postcard {
    position: absolute;
    left: 278px;
    top: 6px;
    width: 702px;
    height: 988px;
    overflow: hidden;
    background:
      radial-gradient(ellipse 70% 55% at 85% 95%, var(--magenta) 0%, rgba(216,52,154,0) 70%),
      radial-gradient(ellipse 60% 50% at 10% 95%, var(--sky) 0%, rgba(90,140,255,0) 70%),
      linear-gradient(160deg, var(--navy) 0%, var(--royal) 38%, var(--violet) 72%, var(--magenta) 100%);
    font-family: "Open Sans", Arial, sans-serif;
  }
  .headline {
    position: absolute;
    margin: 0;
    font-family: "Pacifico", cursive;
    font-weight: 400;
    font-size: 180px;
    color: var(--glow);
    line-height: 1;
    white-space: nowrap;
    text-shadow: 0 0 8px rgba(255,255,255,0.9), 0 0 22px rgba(150,200,255,0.9), 0 0 40px rgba(120,170,255,0.6);
  }
  .headline-happy { left: 78px; top: 92px; }
  .headline-hour { left: 48px; top: 222px; }
  .brand-mark {
    position: absolute;
    left: 472px;
    top: 418px;
    display: flex;
    align-items: center;
    gap: 8px;
    font-weight: 700;
    font-size: 26px;
    color: var(--glow);
    letter-spacing: 1px;
    white-space: nowrap;
  }
  .brand-mark .dot {
    width: 12px; height: 12px; border-radius: 50%; background: var(--glow);
  }
  .offer {
    position: absolute;
    left: 108px;
    margin: 0;
    font-weight: 800;
    color: var(--offer-green);
    font-size: 76px;
    line-height: 1;
    letter-spacing: -0.5px;
    white-space: nowrap;
  }
  .offer-buy { top: 429px; }
  .offer-get { top: 494px; }
  .offer-terms {
    position: absolute;
    left: 114px;
    top: 574px;
    margin: 0;
    font-size: 16.5px;
    font-weight: 700;
    color: var(--ink);
    white-space: nowrap;
  }
  .location-map {
    position: absolute;
    left: 82px;
    top: 644px;
    width: 540px;
    height: 240px;
    border-radius: 6px;
    background: linear-gradient(120deg, var(--map-tone-a), var(--map-tone-b));
  }
  .social {
    position: absolute;
    left: 40px;
    top: 920px;
    display: flex;
    gap: 12px;
    color: var(--glow);
    font-size: 15.5px;
    font-weight: 400;
    white-space: nowrap;
  }
  .social span { display: flex; align-items: center; gap: 6px; }
  .social i {
    display: inline-block; width: 20px; height: 20px; border-radius: 50%;
    background: rgba(255,255,255,0.35);
  }
</style>
</head>
<body>
  <main class="postcard">
    <h1 class="headline headline-happy">Happy</h1>
    <p class="headline headline-hour">Hour</p>

    <div class="brand-mark"><span class="dot"></span>LANTERN 27</div>

    <p class="offer offer-buy">BUY ONE</p>
    <p class="offer offer-get">GET ONE FREE</p>
    <p class="offer-terms">(EXCLUDING CHAMPAGNE) EVERY SUNDAY - FRIDAY UNTIL 8PM</p>

    <div class="location-map" role="img" aria-label="Simple street map showing how to find the bar from nearby roads and rail lines"></div>

    <footer class="social">
      <span><i></i>/LANTERN27</span>
      <span><i></i>@LANTERN27</span>
      <span><i></i>@LANTERN27</span>
      <span><i></i>WWW.LANTERN27.CO.UK</span>
    </footer>
  </main>
</body>
</html>
```